Online ticketing company needs new biz card design

Needing an updated business card to reflect our company, incorporating our existing logo and colour scheme (red, black, white). The design should communicate our modern, online, technology, innovation based company.

Details for card need to include the following:

Name
Position
Telephone and extension number
Mobile number
Email
Web address
Physical and/or postal address

Industry/Entity Type

Business

Font styles to use
Sans Serif

Requirements
Must have
• Clear, bold, eye catching design

```html
<!DOCTYPE html>
<html lang="en">
<head>
<meta charset="utf-8">
<title>TIXORA Business Card</title>
<link href="https://fonts.googleapis.com/css2?family=Varela+Round&family=Arimo:wght@400;700&display=swap" rel="stylesheet">
<style>
  :root {
    --ink: #111111;
    --paper: #ffffff;
    --charcoal: #2f2b2c;
    --backdrop: #d9d9d9;
    --frame-line: #e8e8e8;
  }
  * { margin: 0; padding: 0; box-sizing: border-box; }
  html, body { width: 1200px; height: 1051px; overflow: hidden; }
  body {
    background: var(--backdrop);
    display: flex;
    flex-direction: column;
    align-items: center;
    justify-content: space-evenly;
    font-family: "Varela Round", "Arimo", sans-serif;
  }
  .card {
    width: 860px;
    height: 470px;
    position: relative;
    overflow: hidden;
  }

  /* Back face */
  .card-back { background: var(--charcoal); }
  .card-back .frame {
    position: absolute;
    inset: 34px;
    border: 4px solid var(--frame-line);
    border-radius: 26px;
  }
  .brand-back {
    position: absolute;
    left: 50%; top: 50%;
    transform: translate(-50%, -50%);
    display: flex;
    align-items: center;
    gap: 22px;
  }
  .brand-back .brand-dot {
    width: 46px; height: 46px;
    border-radius: 50%;
    background: var(--paper);
  }
  .brand-back .brand-name {
    color: var(--paper);
    font-size: 92px;
    letter-spacing: 2px;
  }
  .back-web {
    position: absolute;
    right: 60px;
    top: 50%;
    transform: translateY(-50%);
    writing-mode: vertical-rl;
    color: var(--paper);
    font-family: "Arimo", sans-serif;
    font-weight: 700;
    font-size: 20px;
    line-height: 1;
    white-space: nowrap;
  }

  /* Front face */
  .card-front { background: var(--paper); }
  .band { position: absolute; left: 0; right: 0; background: var(--ink); }
  .band-top { top: 0; height: 34px; }
  .band-bottom { bottom: 0; height: 52px; }
  .brand-front {
    position: absolute;
    right: 56px; top: 64px;
    display: flex;
    align-items: center;
    gap: 12px;
  }
  .brand-front .brand-dot {
    width: 26px; height: 26px;
    border-radius: 50%;
    background: var(--ink);
  }
  .brand-front .brand-name {
    color: var(--ink);
    font-size: 44px;
    letter-spacing: 1px;
  }
  .identity {
    position: absolute;
    left: 70px; top: 108px;
    color: var(--ink);
  }
  .identity .person-name { font-size: 48px; line-height: 1.1; font-weight: 400; }
  .identity .person-role { font-size: 25px; margin-top: 2px; }
  .contacts {
    position: absolute;
    left: 70px; top: 226px;
    display: grid;
    grid-template-columns: 112px auto;
    column-gap: 18px;
    row-gap: 1px;
    align-items: baseline;
    color: var(--ink);
  }
  .contacts dt {
    font-family: "Arimo", sans-serif;
    font-size: 17px;
    text-align: right;
  }
  .contacts dd { font-size: 28px; line-height: 1.15; }
</style>
</head>
<body>

  <section class="card card-back" aria-label="Card back">
    <div class="frame"></div>
    <div class="brand-back">
      <span class="brand-dot"></span>
      <span class="brand-name">TIXORA</span>
    </div>
    <div class="back-web">www.yourweb.com</div>
  </section>

  <section class="card card-front" aria-label="Card front">
    <div class="band band-top"></div>
    <div class="brand-front">
      <span class="brand-dot"></span>
      <span class="brand-name">TIXORA</span>
    </div>
    <div class="identity">
      <h1 class="person-name">Your NAME</h1>
      <p class="person-role">Sales Manager / Administator</p>
    </div>
    <dl class="contacts">
      <dt>Phone:</dt><dd>+12 34 567</dd>
      <dt>Mobile:</dt><dd>+12 34 567 89</dd>
      <dt>E-mail:</dt><dd>yourmail@yourweb.com</dd>
      <dt>Web:</dt><dd>www.yourweb.com</dd>
      <dt>Address:</dt><dd>Somewhere "Near or Far" 13</dd>
    </dl>
    <div class="band band-bottom"></div>
  </section>

</body>
</html>
```